Startup Drone Platform Company business card

We are needing a business card design for our employees. We are a startup drone platform. We are looking for a business card that has our logo on one side, with the employee/company details on the opposite side. We are looking for something that is very eye catching, modern, and bold.

Target Market(s)

This will target both drone pilots and drone businesses, along with all the industries that could utilize drone services (aerial video, aerial photos, inspections, 3d mapping, etc).

Industry/Entity Type

Business

```html
<!DOCTYPE html>
<html lang="en">
<head>
<meta charset="utf-8">
<title>SkyHire Hub – Business Card</title>
<link href="https://fonts.googleapis.com/css2?family=Lato:wght@300;400;700;900&family=Open+Sans:wght@400;600;700&display=swap" rel="stylesheet">
<style>
  :root {
    --stage: #2b2b2b;
    --card-dark: #0d0d0d;
    --card-light: #ffffff;
    --card-light-edge: #e9e9e9;
    --teal: #2a9aa3;
    --ink: #1a1a1a;
    --ink-soft: #3a3a3a;
    --silver: #d8d8d8;
  }
  * { box-sizing: border-box; margin: 0; padding: 0; }
  html, body {
    width: 1200px; height: 997px; overflow: hidden;
    background: var(--stage);
  }
  .stage {
    position: relative; width: 1200px; height: 997px;
    display: flex; flex-direction: column; align-items: center; justify-content: center; gap: 60px;
  }
  .card {
    position: relative; width: 640px; height: 366px;
    border-radius: 22px; overflow: hidden;
  }
  /* Back side */
  .card-back {
    background: var(--card-dark);
    display: flex; align-items: center; justify-content: center; gap: 18px;
  }
  .back-brand {
    font-family: "Lato", sans-serif; font-weight: 300;
    font-size: 34px; letter-spacing: 0.42em; color: var(--silver);
    text-transform: uppercase;
  }
  .back-dot {
    width: 18px; height: 18px; border-radius: 50%; background: var(--teal);
  }
  /* Front side */
  .card-front {
    background: linear-gradient(160deg, var(--card-light) 40%, var(--card-light-edge));
  }
  .front-brand {
    position: absolute; left: 48px; top: 96px;
    display: flex; align-items: center; gap: 16px;
  }
  .front-brand-name {
    font-family: "Lato", sans-serif; font-weight: 400;
    font-size: 22px; letter-spacing: 0.5em; color: var(--ink);
    text-transform: uppercase;
  }
  .front-brand-dot {
    width: 12px; height: 12px; border-radius: 50%; background: var(--teal);
  }
  .person {
    position: absolute; left: 48px; top: 196px; right: 40px;
  }
  .person-row { display: flex; align-items: flex-end; gap: 12px; }
  .person-name {
    font-family: "Lato", sans-serif; font-weight: 900;
    font-size: 24px; color: var(--teal); white-space: nowrap;
  }
  .person-rule { flex: 1; height: 2px; background: var(--teal); margin-bottom: 8px; }
  .person-title {
    font-family: "Open Sans", sans-serif; font-weight: 700;
    font-size: 12px; color: var(--ink); letter-spacing: 0.02em; margin-top: 2px;
  }
  .contact {
    position: absolute; left: 48px; top: 272px; list-style: none;
    font-family: "Open Sans", sans-serif; font-size: 15px; color: var(--ink-soft);
  }
  .contact li { display: flex; align-items: center; gap: 14px; height: 24px; }
  .contact-icon { width: 16px; height: 16px; flex: none; }
  .contact-web {
    padding-left: 30px; color: var(--teal); font-weight: 700;
  }
</style>
</head>
<body>
<main class="stage">
  <section class="card card-back" aria-label="Card back">
    <span class="back-brand">SkyHire Hub</span>
    <span class="back-dot"></span>
  </section>

  <section class="card card-front" aria-label="Card front">
    <div class="front-brand">
      <span class="front-brand-name">SkyHire Hub</span>
      <span class="front-brand-dot"></span>
    </div>

    <div class="person">
      <div class="person-row">
        <span class="person-name">Maren Holloway</span>
        <span class="person-rule"></span>
      </div>
      <div class="person-title">FOUNDER &amp; CEO</div>
    </div>

    <ul class="contact">
      <li>
        <svg class="contact-icon" viewBox="0 0 16 16" aria-hidden="true">
          <circle cx="8" cy="8" r="8" fill="var(--teal)"/>
          <path d="M5.2 4.2l1.4 1.6-.7 1.1c.5 1.1 1.2 1.8 2.2 2.3l1.1-.7 1.6 1.4-.8 1.4c-2.9-.3-5.2-2.6-5.5-5.5z" fill="#fff"/>
        </svg>
        <span>+1 (555) 014-2286</span>
      </li>
      <li>
        <svg class="contact-icon" viewBox="0 0 16 16" aria-hidden="true">
          <circle cx="8" cy="8" r="8" fill="var(--teal)"/>
          <path d="M8 3.8l4 3.4h-1.1v4.2H9.2V9H6.8v2.4H5.1V7.2H4z" fill="#fff"/>
        </svg>
        <span>Unit 42, Block 7, Lakeside</span>
      </li>
      <li class="contact-web">www.skyhirehub.com</li>
    </ul>
  </section>
</main>
</body>
</html>
```